Stationery Design Project - New innovative law firm

I need a simple design, yet the tone of the stationery set need to express modern, professionalism, smart and forward-thinking. I don’t need a business card, but require the stationery set to have:
• Design letterhead
• Design facsimile
• Design memo
The triangular logo with Halvard Lane words etc, need to be present in the stationery. The red triangular logo should not be re-designed, but feel free to play around with the placement and colours of the Halvard Lane words etc....?

Target Market(s)

Business clients

Industry/Entity Type

Business

Requirements
Must have
• The triangular logo with Halvard Lane words etc...for branding.

```html
<!DOCTYPE html>
<html lang="en">
<head>
<meta charset="utf-8">
<title>Halvard Lane Letterhead</title>
<link rel="stylesheet" href="https://fonts.googleapis.com/css2?family=Arimo:wght@400;700&family=Source+Sans+3:wght@400;700&display=swap">
<style>
  :root {
    --backdrop: #e9e7e3;
    --paper: #ffffff;
    --brand-red: #d7141c;
    --brand-red-dark: #b5121a;
    --brand-red-light: #ec2a30;
    --band-grey: #77777b;
    --ink: #1d1d1d;
    --rule: #6f6f6f;
  }
  * { margin: 0; padding: 0; box-sizing: border-box; }
  html, body {
    width: 951px; height: 1200px; overflow: hidden;
    background: var(--backdrop);
  }
  .letterhead {
    position: absolute; left: 73px; top: 72px;
    width: 806px; height: 1043px;
    background: var(--paper);
    box-shadow: 0 2px 10px rgba(0,0,0,0.18);
    font-family: "Source Sans 3", "Myriad Pro", sans-serif;
    color: var(--ink);
  }
  .header-band { position: absolute; left: 0; top: 0; width: 806px; height: 200px; display: block; }
  .brand {
    position: absolute; left: 32px; top: 42px;
    display: flex; align-items: flex-start; gap: 14px;
    color: #fff; font-family: "Arimo", Arial, sans-serif;
  }
  .brand-square { width: 14px; height: 14px; background: #fff; margin-top: 12px; }
  .brand-name {
    font-size: 40px; font-weight: 700; line-height: 40px;
    letter-spacing: -0.5px; text-transform: uppercase;
  }
  .brand-tagline {
    margin-top: 4px; font-size: 15.5px; font-weight: 400;
    letter-spacing: 0.1px; text-transform: uppercase;
  }
  .brand-tagline .dot {
    display: inline-block; width: 6px; height: 6px; background: #fff;
    margin: 0 3px; vertical-align: 2px;
  }
  .staff-list {
    position: absolute; left: 630px; top: 151px;
    list-style: none; font-size: 14px; line-height: 18px;
  }
  .footer {
    position: absolute; left: 21px; top: 951px; width: 762px;
    border-top: 1px solid var(--rule);
    text-align: center;
  }
  .footer-contact { margin-top: 17px; font-size: 13.8px; line-height: 18px; }
  .footer-contact .sep { margin: 0 7px; }
  .footer-legal { margin-top: 7px; font-size: 11px; line-height: 14px; }
</style>
</head>
<body>
  <main class="letterhead">
    <svg class="header-band" viewBox="0 0 806 200" aria-hidden="true">
      <defs>
        <linearGradient id="redSweep" x1="0" y1="0" x2="1" y2="0.4">
          <stop offset="0" stop-color="var(--brand-red)"/>
          <stop offset="0.6" stop-color="var(--brand-red-dark)"/>
          <stop offset="1" stop-color="var(--brand-red-light)"/>
        </linearGradient>
      </defs>
      <path d="M0,0 H806 V112 Q420,116 0,174 Z" fill="url(#redSweep)"/>
      <path d="M380,0 Q640,20 806,80 V0 Z" fill="var(--brand-red-light)" opacity="0.45"/>
      <path d="M0,174 Q420,116 806,112 V127 Q420,132 0,196 Z" fill="var(--band-grey)"/>
    </svg>

    <div class="brand">
      <span class="brand-square"></span>
      <div>
        <div class="brand-name">Halvard Lane</div>
        <div class="brand-tagline">Legal<span class="dot"></span>Tax<span class="dot"></span>Accounting &amp; Business Advisors</div>
      </div>
    </div>

    <ul class="staff-list">
      <li>XXX. Director</li>
      <li>XXX. Principal</li>
      <li>XXX. Leagal Consultant</li>
    </ul>

    <footer class="footer">
      <p class="footer-contact">
        418 Marlow Street, Kenby, Qld 4120<span class="sep">|</span>PO Box 3190, Kenby Qld 4120<span class="sep">|</span><strong>Ph :</strong> (07) 5550 1942<span class="sep">|</span><strong>Fax :</strong> (07) 5550 1943
      </p>
      <p class="footer-legal">
        Liability is limited by a scheme approved under professional standards legislation<br>
        Company trading as Coastline Law - incorporating XXX (ABN 987650432)
      </p>
    </footer>
  </main>
</body>
</html>
```